International E-Shop Needs a Web Design

I need a web design for a new e-shop based in UK, called Vornu. This will be an international collective buying website. I would like to see designs that use the colors orange and green (similar to logo colors). However, any other ideas and your vision are also welcome. The brand image is associated with words fun, social, cool and simple. The final design should look very modern and unique. Please also take into consideration user experience.

I have attached logo design. Please ignore the black background, it would be better if you extract only the name Vornu on the logo design. I have also attached one example of website design which I like (especially it's modern style, plumvexa.com) and two screenshots showing icons that visualize each category (which I want to appear in my main menu bar).

*UPDATE: There is something wrong with the system and I can't upload other 3 files (web design example and 2 examples of icons). If you could give me your e-mail, then I could send all these files to you. Anyway, what I think is a modern design can be viewed on plumvexa.com

If you have any further questions, do not hesitate to ask. Thank you in advance and I look forward to your outstanding designs!

Target Market(s)

My target customers are people both male and female in the age group of 18-45 years old, who are shopping online and are present on social media.

Industry/Entity Type

Shop

Requirements
Must have
• - "What is Vornu?" Button
- Log In / Register Buttons
- Currency Sliding Menu
- Shopping Cart
- "How to Buy?" and "How to Sell?" Buttons
- Follow us on Tralmonde, Quenzip, Brasko+
- Like Button with a number of people who like this.
- Check-In Button
- RSS Feed
- Main Menu with categories and buttons, such as Home, Electronics, Entertainment & Leisure, Fashion, Health & Beauty, Home & Garden, Jewellery & Watches, Sports & Outdoors. I would like to see also small pictures (icons) that would symbolize each category.
- Search Bar
- Carousel Slideshow with 5 different slides. The first slide on carousel slideshow should be welcoming! Something like: "Welcome to Vornu! Why to shop at Vornu?" - This slide should be designed in a similar way as the website.
- Four Main Categories: Latest Bargains, Your Recently Viewed Bargains, Ending Soon Bargains, Popular Bargains
- Under Each Category should be at least 3 products
- Users will be allowed to upload their own pictures, which means that picture quality and design will be different. Some kind of frames around pictures or something else (under one style) to make pictures look similar would be very helpful.
- Each Product should show the following information: Main Photo, Name, Description (Short), Total Discount (for example 35%), Current Discount (for example 5%), Starting Price, Current Price, Time Left on Bargain: 7:1:45:30
- The final design should be delivered in Draftline format file (PSD file).
Should not have
• The choice of colors shouldn't be aggressive. Instead it should be calm and gentle. So that the user would feel himself comfortable while browsing the website.

```html
<!DOCTYPE html>
<html lang="en">
<head>
<meta charset="utf-8">
<title>Vornu – Collective Bargains</title>
<link href="https://fonts.googleapis.com/css2?family=Ubuntu:wght@400;500;700&family=Open+Sans:wght@400;600;700&display=swap" rel="stylesheet">
<style>
:root{
  --orange:#f0561d;
  --orange-light:#ff6c2b;
  --orange-dark:#c8461a;
  --green:#8cc63f;
  --green-dark:#6da72b;
  --ink:#2a2a2a;
  --text:#4a4a4a;
  --muted:#666;
  --page:#efefef;
  --white:#fff;
  --black:#151515;
}
*{box-sizing:border-box;margin:0;padding:0}
html,body{width:1058px;height:1200px;overflow:hidden;background:var(--page)}
body{font-family:"Open Sans",Arial,sans-serif;color:var(--text)}
.canvas{position:relative;width:1058px;height:1200px;overflow:hidden;background:var(--page)}
.abs{position:absolute}

/* top bar */
.topbar{left:0;top:0;width:1058px;height:28px;background:linear-gradient(#2b2b2b,#0d0d0d)}
.brand{left:178px;top:3px;font-family:"Ubuntu",sans-serif;font-weight:700;font-size:18px;color:var(--orange);line-height:22px;display:flex;align-items:center;gap:3px;white-space:nowrap}
.brand-dot{width:6px;height:6px;background:var(--green);display:inline-block}
.topnav{left:243px;top:0;height:28px;display:flex;align-items:center;gap:17px;font-family:"Ubuntu",sans-serif;font-size:9.5px;color:#bbb;white-space:nowrap}
.topnav .active{color:#fff;font-weight:700}
.currency{left:754px;top:0;height:28px;display:flex;align-items:center;font-family:"Ubuntu",sans-serif;font-size:9.5px;color:#fff;white-space:nowrap}
.currency-select{margin-left:4px;width:62px;height:12px;background:#fff;border:1px solid #999;font-size:8px;color:#999;padding-left:2px;line-height:10px;position:relative}
.currency-select::after{content:"";position:absolute;right:2px;top:3px;border:3px solid transparent;border-top-color:#777}
.lang{margin-left:5px;width:14px;height:12px;background:var(--orange);color:#fff;font-size:7.5px;font-weight:700;text-align:center;line-height:12px}

/* hero */
.hero{left:0;top:28px;width:1058px;height:269px;background:linear-gradient(90deg,#ee5419,#ff6a28 50%,#ee5419)}
.slide{background:#161616;border:5px solid #d54c1b;border-bottom:none}
.slide-back2{left:178px;top:85px;width:704px;height:212px}
.slide-back1{left:203px;top:72px;width:650px;height:225px}
.slide-main{left:254px;top:45px;width:554px;height:252px;border-width:7px}
.slide-photo{position:absolute;inset:0;background:radial-gradient(ellipse at 58% 55%,#b9b6b0 0%,#7d7b78 35%,#3d3c3b 70%,#1c1c1c 100%)}
.side-photo{position:absolute;top:12px;bottom:0;width:24px;background:linear-gradient(#555,#2a2a2a)}
.hero-title{left:286px;top:72px;font-family:"Ubuntu",sans-serif;color:#fff;line-height:1.15}
.hero-title span{display:block;font-size:21px}
.hero-title strong{display:block;font-size:26px;font-weight:700}

/* action row */
.btn{top:316px;height:22px;font-family:"Ubuntu",sans-serif;font-size:14.5px;line-height:22px;text-align:center;white-space:nowrap;box-shadow:0 1px 2px rgba(0,0,0,.15)}
.btn strong{font-weight:700}
.btn-what{left:178px;width:108px;background:linear-gradient(#e4e4e4,#c9c9c9);color:#333}
.btn-sell{left:298px;width:108px;background:linear-gradient(#9fd64c,var(--green-dark));color:#222}
.btn-buy{left:417px;width:109px;background:linear-gradient(var(--orange-light),var(--orange));color:#fff}
.search{left:536px;top:316px;width:154px;height:22px;border:2px solid #4a90d9;background:#fff;display:flex}
.search-field{flex:1;font-size:9.5px;font-style:italic;color:#9aa;padding-left:6px;line-height:18px}
.search-go{width:25px;background:var(--green);color:#fff;font-size:9.5px;font-weight:700;text-align:center;line-height:18px}
.account{left:698px;top:316px;width:184px;height:22px;background:linear-gradient(90deg,#f2f2f2,#d0d0d0);display:flex;justify-content:flex-end;align-items:center;font-family:"Ubuntu",sans-serif;font-size:10.5px;color:#222;white-space:nowrap}
.account b{font-weight:700}
.account .or{margin:0 4px;font-weight:400}
.signup{background:var(--green);height:18px;line-height:18px;padding:0 4px;margin-right:2px;font-weight:700}

/* panels */
.panel{top:360px;height:114px;background:var(--white)}
.panel-info{left:178px;width:512px;padding:15px 16px;font-size:8.6px;line-height:11px;color:#333}
.panel-info p+p{margin-top:11px}
.panel-cart{left:698px;width:184px}
.pointer{top:348px;width:0;height:0;border-right:10px solid transparent;border-bottom:12px solid var(--white)}
.cart-title{left:8px;top:8px;font-size:9px;color:#333;white-space:nowrap}
.cart-title b{font-weight:700}
.checkout{right:3px;top:3px;background:var(--orange);color:#fff;font-size:8.5px;font-weight:700;padding:0 3px;line-height:13px;white-space:nowrap}
.cart-row{left:8px;right:14px;font-size:8.3px;line-height:10px;color:#222;display:flex;justify-content:space-between}
.cart-row b{font-weight:700}
.cart-item{left:15px;font-size:8px;line-height:9.8px;color:#333;width:80px}
.cart-item b{font-weight:700;display:block}

/* category menu */
.catbar{left:178px;top:485px;width:704px;height:28px;background:linear-gradient(#1c1c1c,#000);display:flex;align-items:center;justify-content:space-between;padding:0 14px 0 5px;font-family:"Ubuntu",sans-serif;font-size:9.7px;color:#eee;white-space:nowrap}
.catbar span{line-height:18px}
.catbar .active{background:#2e2e2e;font-weight:700;color:#fff;padding:0 9px}

/* bargains */
.section-title{font-family:"Ubuntu",sans-serif;font-weight:500;font-size:13px;color:var(--ink);letter-spacing:.2px;white-space:nowrap}
.section-title em{font-style:normal;color:var(--orange)}
.product{width:312px;height:75px}
.product-frame{position:absolute;left:0;top:0;width:106px;height:75px;background:var(--white);box-shadow:0 0 0 1px #e6e6e6}
.product-photo{position:absolute;left:33px;top:8px;width:40px;height:59px;background:linear-gradient(160deg,#c9474f,#6d2f3a 50%,#d6bfa0)}
.product-info{position:absolute;left:117px;top:8px;width:200px;font-size:8.4px;line-height:10.3px;color:var(--muted)}
.product-name{font-size:9.5px;font-weight:700;color:#333}
.product-desc{margin-bottom:3px}
.stats{display:grid;grid-template-columns:70px 31px 70px 30px;white-space:nowrap}
.stats .wide{grid-column:span 2}
.stats .price{font-weight:700;color:#222;font-size:9.3px}

/* social + footer */
.social{left:516px;top:1129px;display:flex;gap:3px}
.social i{width:16px;height:16px;display:block;border-radius:2px}
.footer{left:0;top:1151px;width:1058px;height:49px;background:linear-gradient(#3a3a3a,#262626);font-size:7.8px;color:#9a9a9a;white-space:nowrap}
.footer-copy{left:176px;top:24px}
.footer-menu{left:603px;top:24px;display:flex}
.footer-menu span{margin-right:20px}
</style>
</head>
<body>
<div class="canvas">

  <header class="abs topbar"></header>
  <div class="abs brand">Vornu<i class="brand-dot"></i></div>
  <nav class="abs topnav">
    <span class="active">Home</span><span>New Products</span><span>New Stores</span><span>All Products</span><span>Reviews</span><span>Contacts</span><span>FAQs</span>
  </nav>
  <div class="abs currency">Currencies:<span class="currency-select">US Dollar</span><span class="lang">En</span></div>

  <section class="abs hero"></section>
  <div class="abs slide slide-back2"><div class="side-photo" style="left:0"></div><div class="side-photo" style="right:0"></div></div>
  <div class="abs slide slide-back1"><div class="side-photo" style="left:0"></div><div class="side-photo" style="right:0"></div></div>
  <div class="abs slide slide-main"><div class="slide-photo" role="img" aria-label="Close-up photograph of a carved stone sculpture"></div></div>
  <div class="abs hero-title"><span>Welcome to</span><strong>Vornu</strong></div>

  <div class="abs btn btn-what">What is <strong>Vornu</strong></div>
  <div class="abs btn btn-sell">How to <strong>Sell</strong>?</div>
  <div class="abs btn btn-buy">How to <strong>Buy</strong>?</div>
  <div class="abs search"><span class="search-field">search</span><span class="search-go">Go</span></div>
  <div class="abs account"><b>Log in</b><span class="or">Or</span><span class="signup">Sign Up</span></div>

  <div class="abs pointer" style="left:198px"></div>
  <div class="abs pointer" style="left:716px"></div>

  <div class="abs panel panel-info">
    <p>This is Draftline's version of Lorem Ipsum. Proin gravida nibh vel velit auctor aliquet. Aenean sollicitudin, lorem quis bibendum auctor, nisi elit consequat ipsum, nec sagittis sem nibh id elit. Duis sed odio sit amet nibh vulputate cursus a sit amet mauris. Morbi accumsan ipsum velit. Nam nec tellus a odio tincidunt auctor a ornare odio.</p>
    <p>Sed non mauris vitae erat consequat auctor eu in elit. Class aptent taciti sociosqu ad litora torquent per conubia nostra, per inceptos himenaeos. Mauris in erat justo. Nullam ac urna eu felis dapibus condimentum sit amet a augue. Sed non neque elit. Sed ut imperdiet nisi. Proin condimentum fermentum nunc. Etiam pharetra, erat sed fermentum feugiat, velit mauris egestas quam, ut aliquam massa nisl quis neque. Suspendisse in orci enim.</p>
  </div>

  <aside class="abs panel panel-cart">
    <div class="abs cart-title">My <b>Digital Cart</b></div>
    <div class="abs checkout">Check Out</div>
    <div class="abs cart-row" style="top:28px"><b>Total Amount</b><b>$480</b></div>
    <div class="abs cart-item" style="top:42px"><b>Item 1</b>Description of the item goes here</div>
    <div class="abs cart-row" style="top:42px;left:120px"><span></span><b>$240</b></div>
    <div class="abs cart-item" style="top:78px"><b>Item 1</b>Description of the item goes here</div>
    <div class="abs cart-row" style="top:78px;left:120px"><span></span><b>$240</b></div>
  </aside>

  <nav class="abs catbar">
    <span class="active">Home</span><span>Electronics</span><span>Entertainment &amp; Leisure</span><span>Fashion</span><span>Health &amp; Beauty</span><span>Home &amp; Garden</span><span>Jewellery &amp; Watches</span><span>Sports &amp; Outdoors</span>
  </nav>

  <h2 class="abs section-title" style="left:179px;top:531px">LATEST <em>BARGAINS</em></h2>
  <h2 class="abs section-title" style="left:570px;top:531px">YOUR RECENTLY VIEWD <em>BARGAINS</em></h2>
  <h2 class="abs section-title" style="left:176px;top:834px">CLOSING SOON <em>BARGAINS</em></h2>
  <h2 class="abs section-title" style="left:570px;top:834px">MOST POPULAR <em>BARGAINS</em></h2>

  <article class="abs product" style="left:178px;top:558px"><div class="product-frame"><div class="product-photo" role="img" aria-label="Product photo: stack of cosmetics"></div></div><div class="product-info"><div class="product-name">Product name</div><div class="product-desc">A very short description of the product goes here description continues.</div><div class="stats"><span>Total Discount</span><span>35%</span><span>Current Discount</span><span>5%</span><span>Starting Price</span><span>$345</span><span>Current Price</span><span class="price">$298</span><span class="wide">Time left for bargain</span><span>7:1:45:30</span><span></span></div></div></article>
  <article class="abs product" style="left:178px;top:643px"><div class="product-frame"><div class="product-photo" role="img" aria-label="Product photo: stack of cosmetics"></div></div><div class="product-info"><div class="product-name">Product name</div><div class="product-desc">A very short description of the product goes here description continues.</div><div class="stats"><span>Total Discount</span><span>35%</span><span>Current Discount</span><span>5%</span><span>Starting Price</span><span>$345</span><span>Current Price</span><span class="price">$298</span><span class="wide">Time left for bargain</span><span>7:1:45:30</span><span></span></div></div></article>
  <article class="abs product" style="left:178px;top:728px"><div class="product-frame"><div class="product-photo" role="img" aria-label="Product photo: stack of cosmetics"></div></div><div class="product-info"><div class="product-name">Product name</div><div class="product-desc">A very short description of the product goes here description continues.</div><div class="stats"><span>Total Discount</span><span>35%</span><span>Current Discount</span><span>5%</span><span>Starting Price</span><span>$345</span><span>Current Price</span><span class="price">$298</span><span class="wide">Time left for bargain</span><span>7:1:45:30</span><span></span></div></div></article>

  <article class="abs product" style="left:572px;top:558px"><div class="product-frame"><div class="product-photo" role="img" aria-label="Product photo: stack of cosmetics"></div></div><div class="product-info"><div class="product-name">Product name</div><div class="product-desc">A very short description of the product goes here description continues.</div><div class="stats"><span>Total Discount</span><span>35%</span><span>Current Discount</span><span>5%</span><span>Starting Price</span><span>$345</span><span>Current Price</span><span class="price">$298</span><span class="wide">Time left for bargain</span><span>7:1:45:30</span><span></span></div></div></article>
  <article class="abs product" style="left:572px;top:643px"><div class="product-frame"><div class="product-photo" role="img" aria-label="Product photo: stack of cosmetics"></div></div><div class="product-info"><div class="product-name">Product name</div><div class="product-desc">A very short description of the product goes here description continues.</div><div class="stats"><span>Total Discount</span><span>35%</span><span>Current Discount</span><span>5%</span><span>Starting Price</span><span>$345</span><span>Current Price</span><span class="price">$298</span><span class="wide">Time left for bargain</span><span>7:1:45:30</span><span></span></div></div></article>
  <article class="abs product" style="left:572px;top:728px"><div class="product-frame"><div class="product-photo" role="img" aria-label="Product photo: stack of cosmetics"></div></div><div class="product-info"><div class="product-name">Product name</div><div class="product-desc">A very short description of the product goes here description continues.</div><div class="stats"><span>Total Discount</span><span>35%</span><span>Current Discount</span><span>5%</span><span>Starting Price</span><span>$345</span><span>Current Price</span><span class="price">$298</span><span class="wide">Time left for bargain</span><span>7:1:45:30</span><span></span></div></div></article>

  <article class="abs product" style="left:178px;top:861px"><div class="product-frame"><div class="product-photo" role="img" aria-label="Product photo: stack of cosmetics"></div></div><div class="product-info"><div class="product-name">Product name</div><div class="product-desc">A very short description of the product goes here description continues.</div><div class="stats"><span>Total Discount</span><span>35%</span><span>Current Discount</span><span>5%</span><span>Starting Price</span><span>$345</span><span>Current Price</span><span class="price">$298</span><span class="wide">Time left for bargain</span><span>7:1:45:30</span><span></span></div></div></article>
  <article class="abs product" style="left:178px;top:946px"><div class="product-frame"><div class="product-photo" role="img" aria-label="Product photo: stack of cosmetics"></div></div><div class="product-info"><div class="product-name">Product name</div><div class="product-desc">A very short description of the product goes here description continues.</div><div class="stats"><span>Total Discount</span><span>35%</span><span>Current Discount</span><span>5%</span><span>Starting Price</span><span>$345</span><span>Current Price</span><span class="price">$298</span><span class="wide">Time left for bargain</span><span>7:1:45:30</span><span></span></div></div></article>
  <article class="abs product" style="left:178px;top:1031px"><div class="product-frame"><div class="product-photo" role="img" aria-label="Product photo: stack of cosmetics"></div></div><div class="product-info"><div class="product-name">Product name</div><div class="product-desc">A very short description of the product goes here description continues.</div><div class="stats"><span>Total Discount</span><span>35%</span><span>Current Discount</span><span>5%</span><span>Starting Price</span><span>$345</span><span>Current Price</span><span class="price">$298</span><span class="wide">Time left for bargain</span><span>7:1:45:30</span><span></span></div></div></article>

  <article class="abs product" style="left:572px;top:861px"><div class="product-frame"><div class="product-photo" role="img" aria-label="Product photo: stack of cosmetics"></div></div><div class="product-info"><div class="product-name">Product name</div><div class="product-desc">A very short description of the product goes here description continues.</div><div class="stats"><span>Total Discount</span><span>35%</span><span>Current Discount</span><span>5%</span><span>Starting Price</span><span>$345</span><span>Current Price</span><span class="price">$298</span><span class="wide">Time left for bargain</span><span>7:1:45:30</span><span></span></div></div></article>
  <article class="abs product" style="left:572px;top:946px"><div class="product-frame"><div class="product-photo" role="img" aria-label="Product photo: stack of cosmetics"></div></div><div class="product-info"><div class="product-name">Product name</div><div class="product-desc">A very short description of the product goes here description continues.</div><div class="stats"><span>Total Discount</span><span>35%</span><span>Current Discount</span><span>5%</span><span>Starting Price</span><span>$345</span><span>Current Price</span><span class="price">$298</span><span class="wide">Time left for bargain</span><span>7:1:45:30</span><span></span></div></div></article>
  <article class="abs product" style="left:572px;top:1031px"><div class="product-frame"><div class="product-photo" role="img" aria-label="Product photo: stack of cosmetics"></div></div><div class="product-info"><div class="product-name">Product name</div><div class="product-desc">A very short description of the product goes here description continues.</div><div class="stats"><span>Total Discount</span><span>35%</span><span>Current Discount</span><span>5%</span><span>Starting Price</span><span>$345</span><span>Current Price</span><span class="price">$298</span><span class="wide">Time left for bargain</span><span>7:1:45:30</span><span></span></div></div></article>

  <div class="abs social">
    <i style="background:#f7931e" aria-label="RSS feed"></i>
    <i style="background:#f5a623" aria-label="Check-in"></i>
    <i style="background:#3b5998" aria-label="Tralmonde"></i>
    <i style="background:#d9d9d9" aria-label="Like"></i>
    <i style="background:#33a8e0" aria-label="Quenzip"></i>
    <i style="background:#e8408a" aria-label="Brasko+"></i>
  </div>

  <footer class="abs footer">
    <div class="abs footer-copy">Copyright @ 2012 your store. All Rights Reserved. Powerd by Lumtrace.</div>
    <div class="abs footer-menu"><span>Additional Menu 1</span><span>Menu2</span><span>Menu3</span><span>Menu4</span><span>Menu5</span><span>Menu6</span></div>
  </footer>

</div>
</body>
</html>
```